Dental Business Card

We are looking for a double sided business card that can be easily customized with the names of the different members of our dental team.

I would like the background to be the 2-tone blue fleur-de-lis type pattern on the sides of our website (www.harborvalebrights.com).

I would like the logo attached incorporated.

I would like our address (2847 Birchmont Court, Suite 100, Elm Bay, OR 97299), phone number (555-318-4902), fax number (555-318-4977), website (www.harborvalebrights.com), and email address (info@harborvalebrights.com) all included on the front side.

Something a little more artistic to complement/highlight the logo on the back would be interesting.

I would like the business card to look professional, slightly feminine, and expense.

```html
<!DOCTYPE html>
<html lang="en">
<head>
<meta charset="utf-8">
<title>Harborvale Brights – Business Card</title>
<link rel="stylesheet" href="https://fonts.googleapis.com/css2?family=Cinzel:wght@400;600&family=Roboto:wght@400;700&display=swap">
<style>
  :root {
    --page-bg: #eef0f2;
    --card-bg: #ffffff;
    --blue-deep: #0b5fa5;
    --blue-mid: #1a86c8;
    --blue-soft: #8fd2ee;
    --blue-pale: #cdeaf7;
    --ink: #2b2b2b;
    --name-grey: #6d6d6d;
    --white: #ffffff;
  }
  html, body {
    margin: 0;
    padding: 0;
    width: 1200px;
    height: 1000px;
    overflow: hidden;
    background: var(--page-bg);
  }
  .canvas {
    position: relative;
    width: 1200px;
    height: 1000px;
  }
  .card {
    position: absolute;
    top: 345px;
    width: 540px;
    height: 309px;
    background: var(--card-bg);
    box-shadow: 0 6px 22px rgba(0,0,0,0.14);
    overflow: hidden;
  }
  .card--back { left: 45px; }
  .card--front { left: 615px; }

  /* Back side */
  .bubble-field {
    position: absolute;
    inset: 0;
    background:
      radial-gradient(ellipse 55% 45% at 15% 10%, var(--blue-soft) 0%, rgba(143,210,238,0.35) 45%, transparent 75%),
      radial-gradient(ellipse 40% 45% at 92% 95%, var(--blue-soft) 0%, rgba(143,210,238,0.35) 45%, transparent 75%),
      radial-gradient(ellipse 30% 30% at 70% 15%, var(--blue-pale) 0%, transparent 70%);
  }
  .back-brand {
    position: absolute;
    inset: 0;
    display: flex;
    flex-direction: column;
    align-items: center;
    justify-content: center;
  }
  .back-brand__mark {
    width: 46px;
    height: 46px;
    border-radius: 50%;
    background: var(--blue-mid);
    margin-bottom: 14px;
  }
  .back-brand__name {
    font-family: "Cinzel", serif;
    font-weight: 600;
    font-size: 40px;
    color: var(--blue-deep);
    letter-spacing: 1px;
    line-height: 1;
  }
  .back-brand__tagline {
    display: flex;
    align-items: center;
    gap: 12px;
    margin-top: 8px;
    width: 470px;
  }
  .back-brand__rule {
    flex: 1;
    height: 2px;
    background: var(--blue-deep);
  }
  .back-brand__tagline-text {
    font-family: "Cinzel", serif;
    font-weight: 600;
    font-size: 19px;
    color: var(--blue-deep);
    letter-spacing: 1px;
  }

  /* Front side */
  .front-brand {
    position: absolute;
    left: 30px;
    top: 34px;
    display: flex;
    align-items: center;
    gap: 10px;
  }
  .front-brand__mark {
    width: 30px;
    height: 30px;
    border-radius: 50%;
    background: var(--blue-mid);
  }
  .front-brand__name {
    font-family: "Cinzel", serif;
    font-weight: 600;
    font-size: 22px;
    color: var(--blue-deep);
  }
  .member-name {
    position: absolute;
    right: 26px;
    top: 88px;
    font-family: "Roboto", sans-serif;
    font-weight: 700;
    font-size: 28px;
    color: var(--name-grey);
  }
  .contact-list {
    position: absolute;
    right: 26px;
    top: 130px;
    margin: 0;
    padding: 0;
    list-style: none;
    text-align: right;
    font-family: "Roboto", sans-serif;
    font-weight: 700;
    font-size: 13px;
    line-height: 19px;
    color: var(--ink);
  }
  .wave-band {
    position: absolute;
    left: 0;
    bottom: 0;
    width: 540px;
    height: 309px;
  }
  .address {
    position: absolute;
    left: 22px;
    bottom: 20px;
    font-family: "Roboto", sans-serif;
    font-weight: 700;
    font-size: 14px;
    color: var(--white);
  }
</style>
</head>
<body>
<main class="canvas">

  <section class="card card--back" aria-label="Business card back">
    <div class="bubble-field" role="img" aria-label="Soft pattern of light blue bubbles scattered around the corners"></div>
    <div class="back-brand">
      <div class="back-brand__mark"></div>
      <div class="back-brand__name">Harborvale Brights</div>
      <div class="back-brand__tagline">
        <span class="back-brand__rule"></span>
        <span class="back-brand__tagline-text">GENTLE CARE, BRIGHT DAYS</span>
        <span class="back-brand__rule"></span>
      </div>
    </div>
  </section>

  <section class="card card--front" aria-label="Business card front">
    <svg class="wave-band" viewBox="0 0 540 309" aria-hidden="true">
      <path d="M0 140 C 120 120, 200 170, 290 230 C 360 275, 430 290, 540 280 L540 309 L0 309 Z" fill="var(--blue-mid)"/>
      <path d="M0 165 C 120 150, 200 195, 280 250 C 340 290, 420 305, 540 300 L540 309 L0 309 Z" fill="var(--blue-deep)"/>
    </svg>

    <div class="front-brand">
      <span class="front-brand__mark"></span>
      <span class="front-brand__name">Harborvale Brights</span>
    </div>

    <div class="member-name">Your Name Here</div>

    <ul class="contact-list">
      <li>fax 555-318-4977</li>
      <li>phone 555-318-4902</li>
      <li>website www.harborvalebrights.com</li>
      <li>email address info@harborvalebrights.com</li>
    </ul>

    <div class="address">2847 Birchmont Court, Suite 100, Elm Bay, OR 97299</div>
  </section>

</main>
</body>
</html>
```